Need high-end luxury business cards with raised element of logo

Looking for a non-standard business card with the option of part of our logo elements to be printed as raised or embossed. Would like at least 5 different photos on the backside. Looking at printing through this: https://www.cardvellox.com/raised-spot-uv-business-cards.html

updated the logo file

```html
<!DOCTYPE html>
<html lang="en">
<head>
<meta charset="utf-8">
<title>Belmora Lane – Business Card</title>
<link rel="stylesheet" href="https://fonts.googleapis.com/css2?family=Montserrat:wght@400;500;700&display=swap">
<style>
  :root {
    --backdrop: #e4e4e4;
    --paper: #ffffff;
    --ink: #3d5a70;
    --ink-soft: #5c6f7e;
    --rule: #8a9aa6;
    --back-top: #3e5d75;
    --back-bottom: #4d7190;
    --raised: rgba(160, 200, 230, 0.32);
    --raised-line: rgba(150, 190, 220, 0.28);
    --highlight: #ffffff;
  }
  * { box-sizing: border-box; margin: 0; padding: 0; }
  html, body { width: 1200px; height: 801px; overflow: hidden; }
  body {
    background: var(--backdrop);
    font-family: "Montserrat", Arial, sans-serif;
    position: relative;
  }
  .card {
    position: absolute;
    top: 258px;
    width: 500px;
    height: 286px;
    border-radius: 4px;
    box-shadow: 0 6px 18px rgba(0,0,0,0.12);
    overflow: hidden;
  }
  .card-front { left: 70px; background: var(--paper); display: flex; }
  .card-back {
    left: 630px;
    background: linear-gradient(160deg, var(--back-top) 0%, var(--back-top) 40%, var(--back-bottom) 100%);
  }
  .brand {
    width: 50%;
    display: flex;
    align-items: center;
    justify-content: center;
  }
  .brand-name {
    color: var(--ink);
    font-weight: 500;
    font-size: 23px;
    letter-spacing: 3px;
  }
  .divider {
    width: 1px;
    background: var(--rule);
    margin: 44px 0;
  }
  .details {
    flex: 1;
    padding: 46px 0 0 26px;
    color: var(--ink-soft);
    font-size: 13px;
    line-height: 1.45;
  }
  .person-name {
    color: var(--ink);
    font-weight: 700;
    font-size: 17px;
    letter-spacing: 0.5px;
  }
  .person-title { margin-bottom: 12px; }
  .address { margin-bottom: 12px; }
  .contact { display: flex; align-items: center; gap: 7px; }
  .contact svg { width: 11px; height: 11px; flex: none; }

  /* raised spot UV pattern on the back */
  .uv-pattern {
    position: absolute;
    inset: 0;
    display: flex;
    flex-direction: column;
  }
  .uv-row {
    flex: 1;
    display: flex;
    align-items: center;
    justify-content: space-around;
    border-bottom: 1px solid var(--raised-line);
  }
  .uv-row:last-child { border-bottom: none; }
  .uv-row.offset { padding-left: 60px; }
  .uv-mark {
    color: var(--raised);
    font-weight: 500;
    font-size: 11px;
    letter-spacing: 2px;
    white-space: nowrap;
  }
  .uv-mark.accent { color: var(--highlight); }
</style>
</head>
<body>
  <section class="card card-front">
    <div class="brand">
      <span class="brand-name">BELMORA LANE</span>
    </div>
    <div class="divider"></div>
    <div class="details">
      <p class="person-name">OWEN CALDER</p>
      <p class="person-title">President</p>
      <p class="address">31275 Marlow Bay Harbor<br>Marlow Bay CA 92870</p>
      <p class="contact">
        <svg viewBox="0 0 12 12" aria-hidden="true"><path fill="#3d5a70" d="M2.5 1l2 2.5-1.2 1.3a7 7 0 003.9 3.9L8.5 7.5 11 9.5 9.8 11C5 10.5 1.5 7 1 2.2z"/></svg>
        555-014-2287
      </p>
      <p class="contact">
        <svg viewBox="0 0 12 12" aria-hidden="true"><path d="M1 2.5h10v7H1z M1 2.5l5 4 5-4" fill="none" stroke="#3d5a70" stroke-width="1.2"/></svg>
        owen@belmoralane.com
      </p>
      <p class="contact">
        <svg viewBox="0 0 12 12" aria-hidden="true"><circle cx="6" cy="6" r="5" fill="none" stroke="#3d5a70" stroke-width="1.2"/><path d="M1 6h10M6 1c-2.5 3-2.5 7 0 10M6 1c2.5 3 2.5 7 0 10" fill="none" stroke="#3d5a70" stroke-width="1"/></svg>
        www.belmoralane.com
      </p>
    </div>
  </section>

  <section class="card card-back" aria-label="Raised spot UV repeat of the brand name across a slate blue card back">
    <div class="uv-pattern">
      <div class="uv-row"><span class="uv-mark">BELMORA LANE</span><span class="uv-mark">BELMORA LANE</span><span class="uv-mark">BELMORA LANE</span></div>
      <div class="uv-row offset"><span class="uv-mark">BELMORA LANE</span><span class="uv-mark">BELMORA LANE</span><span class="uv-mark">BELMORA LANE</span></div>
      <div class="uv-row"><span class="uv-mark">BELMORA LANE</span><span class="uv-mark">BELMORA LANE</span><span class="uv-mark">BELMORA LANE</span></div>
      <div class="uv-row offset"><span class="uv-mark">BELMORA LANE</span><span class="uv-mark">BELMORA LANE</span><span class="uv-mark">BELMORA LANE</span></div>
      <div class="uv-row"><span class="uv-mark">BELMORA LANE</span><span class="uv-mark">BELMORA LANE</span><span class="uv-mark accent">BELMORA LANE</span></div>
      <div class="uv-row offset"><span class="uv-mark">BELMORA LANE</span><span class="uv-mark">BELMORA LANE</span><span class="uv-mark">BELMORA LANE</span></div>
    </div>
  </section>
</body>
</html>
```